Bref créative
Stationery for bright harbor company
Stationery for my company
Professional
Farhan Tariq Baloch
General Manager
Prince Faisal Street,
Al Warood,
Riyadh,
Saudi Arabia.
P.O.Box:5831-6-40921-3158.
farhan@br1ghth4rb0r.example
www.br1ghth4rb0r.example
C.R.
I want something creative, plus if it is possible can you put the information editable so I can put the other names and titles for the other co - workers
My logo or something creative
logo to be used
like this

```html
<!DOCTYPE html>
<html lang="en">
<head>
<meta charset="utf-8">
<title>Bright Harbor Company Stationery Concept</title>
<link rel="stylesheet" href="https://fonts.googleapis.com/css2?family=Arimo:wght@400;700&family=Roboto:wght@400;700&display=swap">
<style>
:root{
  --board:#2a2c2e;
  --board-dark:#1c1d1f;
  --label:#e9ecef;
  --paper:#ffffff;
  --brand:#2f6d95;
  --brand-dark:#1d4a69;
  --brand-light:#5b9cc4;
  --ink:#3b4248;
  --muted:#8a949c;
  --grey-flap:#6d7277;
}
*{box-sizing:border-box;margin:0;padding:0}
html,body{width:1200px;height:425px;overflow:hidden;background:var(--board-dark)}
.board{position:relative;width:1200px;height:425px;overflow:hidden;
  background:radial-gradient(ellipse at 50% 40%,#3a3d40 0%,var(--board) 55%,var(--board-dark) 100%);
  font-family:"Arimo",Arial,sans-serif;color:var(--ink)}
.board-title{position:absolute;left:12px;top:10px;font-size:17px;font-weight:700;color:var(--label)}
.section-label{position:absolute;font-size:13px;color:var(--label);white-space:nowrap}
.piece{position:absolute;background:var(--paper);box-shadow:0 3px 8px rgba(0,0,0,.55);overflow:hidden}

.brand{display:flex;align-items:center;gap:4px;font-family:"Roboto",Arial,sans-serif;font-weight:700;color:var(--brand-dark);letter-spacing:.5px;white-space:nowrap}
.brand-dot{border-radius:50%;background:var(--brand);flex:none}
.brand.on-dark{color:#fff}
.brand.on-dark .brand-dot{background:#fff}

.card{width:183px;height:68px}
.card-front-a{left:19px;top:120px}
.card-front-b{left:19px;top:199px}
.card-back{left:19px;top:281px;height:72px;background:linear-gradient(135deg,var(--brand-light),var(--brand) 55%,var(--brand-dark))}
.card-front-a .brand{position:absolute;left:50px;top:22px;font-size:8px}
.card-front-a .brand-dot{width:14px;height:14px}
.card-front-a .strip{position:absolute;left:0;right:0;top:40px;height:4px;background:var(--brand)}
.card-person{position:absolute;font-size:4.5px;line-height:6px;color:var(--ink);white-space:nowrap}
.card-person strong{color:var(--brand-dark)}
.card-front-a .card-person{left:70px;top:48px}
.card-front-b .brand{position:absolute;left:14px;top:12px;font-size:7px}
.card-front-b .brand-dot{width:12px;height:12px}
.card-front-b .card-person{left:14px;top:30px}
.card-front-b .bar{position:absolute;left:0;right:0;bottom:0;height:6px;background:var(--brand)}
.card-back .brand{position:absolute;left:50%;top:50%;transform:translate(-50%,-50%);font-size:10px}
.card-back .brand-dot{width:16px;height:16px}

.letterhead{width:206px;height:336px;top:72px}
.letterhead-a{left:223px}
.letterhead-b{left:456px}
.letterhead .brand{position:absolute;left:50%;top:24px;transform:translateX(-50%);font-size:7px}
.letterhead .brand-dot{width:12px;height:12px}
.letter-footer{position:absolute;left:0;right:0;bottom:8px;height:7px;background:linear-gradient(90deg,var(--brand-dark),var(--brand-light))}
.letter-footer-text{position:absolute;left:0;right:0;bottom:18px;text-align:center;font-size:3.6px;color:var(--muted);white-space:nowrap}

.envelope{width:213px;height:96px}
.env-a{left:713px;top:77px}
.env-b{left:713px;top:212px}
.env-c{left:713px;top:336px;height:74px}
.env-d{left:950px;top:77px}
.env-e{left:950px;top:206px}
.env-f{left:950px;top:326px;height:84px}
.env-flap{position:absolute;left:0;top:0;width:100%;height:40px}
.env-d .brand,.env-e .brand,.env-f .brand{position:absolute;left:14px;top:12px;font-size:6px}
.envelope .brand-dot{width:10px;height:10px}
.env-address{position:absolute;left:14px;top:27px;font-size:3.6px;line-height:5px;color:var(--muted)}
.env-rule{position:absolute;left:0;right:0;bottom:6px;height:3px;background:var(--brand)}
.env-a .brand,.env-c .brand{position:absolute;left:50%;top:10px;transform:translateX(-50%);font-size:6px}
</style>
</head>
<body>
<main class="board">
  <h1 class="board-title">Stationary Concept</h1>

  <p class="section-label" style="left:14px;top:98px">Bussiness Card Front</p>
  <p class="section-label" style="left:378px;top:38px">Leltter Head Concept</p>
  <p class="section-label" style="left:830px;top:38px">Envoulpe Concept</p>
  <p class="section-label" style="left:18px;top:360px">Bussiness Card Back</p>

  <div class="piece card card-front-a">
    <div class="brand"><span class="brand-dot"></span>BRIGHTHARBOR</div>
    <div class="strip"></div>
    <div class="card-person"><strong>Staff Name</strong> · Job Title · name@brightharbor.example</div>
  </div>
  <div class="piece card card-front-b">
    <div class="brand"><span class="brand-dot"></span>BRIGHTHARBOR</div>
    <div class="card-person"><strong>Staff Name</strong><br>Job Title<br>www.brightharbor.example</div>
    <div class="bar"></div>
  </div>
  <div class="piece card card-back">
    <div class="brand on-dark"><span class="brand-dot"></span>BRIGHTHARBOR</div>
  </div>

  <div class="piece letterhead letterhead-a">
    <div class="brand"><span class="brand-dot"></span>BRIGHTHARBOR</div>
    <p class="letter-footer-text">Street Name, District, City, Country · Phone 000 000 0000 · www.brightharbor.example</p>
    <div class="letter-footer"></div>
  </div>
  <div class="piece letterhead letterhead-b">
    <div class="brand"><span class="brand-dot"></span>BRIGHTHARBOR</div>
    <p class="letter-footer-text">Street Name, District, City, Country · Phone 000 000 0000 · www.brightharbor.example</p>
    <div class="letter-footer"></div>
  </div>

  <div class="piece envelope env-a">
    <svg class="env-flap" viewBox="0 0 213 40" preserveAspectRatio="none">
      <path d="M0 0H213V22Q106.5 46 0 22Z" fill="var(--brand)"/>
    </svg>
    <div class="brand on-dark"><span class="brand-dot"></span>BRIGHTHARBOR</div>
  </div>
  <div class="piece envelope env-b">
    <svg class="env-flap" viewBox="0 0 213 40" preserveAspectRatio="none">
      <path d="M0 22Q106.5 46 213 22" fill="none" stroke="#d4d9de" stroke-width="1.2"/>
    </svg>
  </div>
  <div class="piece envelope env-c">
    <svg class="env-flap" viewBox="0 0 213 40" preserveAspectRatio="none">
      <path d="M0 0H213V22Q106.5 46 0 22Z" fill="var(--grey-flap)"/>
    </svg>
    <div class="brand on-dark"><span class="brand-dot"></span>BRIGHTHARBOR</div>
  </div>

  <div class="piece envelope env-d">
    <div class="brand"><span class="brand-dot"></span>BRIGHTHARBOR</div>
    <p class="env-address">Street Name, District,<br>City, Country.</p>
    <div class="env-rule"></div>
  </div>
  <div class="piece envelope env-e">
    <div class="brand"><span class="brand-dot"></span>BRIGHTHARBOR</div>
    <p class="env-address">Street Name, District,<br>City, Country.</p>
    <div class="env-rule"></div>
  </div>
  <div class="piece envelope env-f">
    <div class="brand"><span class="brand-dot"></span>BRIGHTHARBOR</div>
    <p class="env-address">Street Name, District,<br>City, Country.</p>
    <div class="env-rule"></div>
  </div>
</main>
</body>
</html>
```